International sports trophy business needs a web design

We need two pages designed for a new company called medalnook. We sell innovative sports trophies via our website and store details of past purchases to allow returning customers to easily place their orders. Customers can log into their accounts using chatterlane or a secondary account login button. The final design should be clean and should focus on the theme of winning the trophy as it is applicable to all sports.

The page should be designed with themes that can be used throughout the site that we'll turn into a cms theme.
Updates

Hi All,

We're half way in to the competition now and I thought it'd be a good time to provide an update on how things are progressing.  First let me thank you for taking part, there's some really great ideas happening here however some of you have requested a mockup for the second page.  I've put that up now and you should be able to find it in the files section of the brief.  Hopefully this will give people a better starting point than before.

To everybody who is still waiting for feedback, be patient, I'm currently working my way through the designs and will be in contact shortly.  I thought in the meantime I could provide a general update as to how I think the competition is progressing and the concepts that I like the most so far. 

For the landing page... The designs that are leading at the moment are not busy or crowded and devote most of the page layout to the front page info-graphic.  The logo, login and primary menu are all easy to identify but not where your eye lands when viewing the page.  The copyright information and secondary menus are there if you look for them.  As far as the style goes we've found that some of the designs feel a little too serious and too adult and we'd like a more playful feel, if you think that your design already is playful, then we probably do too.  Finally I'll add that we like our logo, but that doesn't mean that we want to see it more than once on the landing page (it's pointless and designs that do this will be unlikely to win) and we certainly do not want to see people creating a new logo or changing our name to nook medal.

For the trophy sales page... There are fewer designs done to this specification as some are unwilling to invest the time in design or unwilling to work without a mockup.  The mockup has now been uploaded to the site (we did want to see what kind of ideas would come here if we didn't include one, thanks to those who had a shot).  If you have any other query about the sales page feel free to contact us.

A final general comment, we want to make sure that all of the images used in your designs are not infringing copyright (this includes images in our mockups, we can only guarantee that we own the copyright for the medalnook logo.).

Hi all, the sliders below have been updated to reflect the more playful design feel that we prefer so far.

Target Market(s)

Our target market is sporting and youth focused but must be adult friendly.

Industry/Entity Type

Business

Requirements
Must have
• We want two pages designed, a landing page and a product display page. We would like a common border scheme across both showing the logo (attached) in the top corner, and secondary links along the bottom.

Landing Page - Must Haves

We see trophies as a representation of achievement and something that can be shared with friends and family. We would like to convey this message in a graphic or illustration on the landing page. Currently in the mockup we have a bunch of trophies, this should not be the final image here.

We have attached a wireframe for the basic format that we'd like to see, you're free to expand upon this as you see fit.

Product Display Page - Must Haves

The product display page will feature a coverflow type device that holds images of the available trophies. It should show the category of the trophy, in this case choose a specific sport to feature (up to you). There should be space for the details of the trophy including price, dimensions, product name, product code, material. There should be room on the page for advertising, this will be common throughout the site except for the landing page. You should include buttons to allow you to add the trophy to your shopping cart and a shopping cart graphic somewhere on the page. There should be a menu bar, unique to this page, that allows a user to choose a new trophy to buy, view previous purchases, view current cart and account settings.

Should not have
• The design should be sport neutral, so don't focus on a single sport or category of sports or sports particular to a certain nationality. With that it's probably easier to just focus on the trophy and achievement aspect rather than the sport being played.

```html
<!DOCTYPE html>
<html lang="en">
<head>
<meta charset="utf-8">
<title>medalnook – Welcome</title>
<link href="https://fonts.googleapis.com/css2?family=Arimo:wght@400;700&display=swap" rel="stylesheet">
<style>
  :root {
    --page-dark: #151515;
    --field-green: #2e4a22;
    --panel-white: #ffffff;
    --nav-dark: #262626;
    --nav-line: #1d5fa8;
    --hero-line: #5d89b0;
    --sky-top: #0f6ab4;
    --sky-bottom: #3be4f2;
    --floor-top: #c9cdd0;
    --floor-bottom: #ffffff;
    --link-blue: #0a76c4;
    --text-dark: #333333;
    --text-white: #ffffff;
    --button-dark: #2b2b2b;
    --button-accent: #d7a514;
    --social-blue: #4a64a0;
    --silver: #dcdcdc;
    --gold-light: #f6dc72;
    --gold-dark: #a7801f;
    --bronze: #d9822e;
  }
  * { box-sizing: border-box; margin: 0; padding: 0; }
  html, body { width: 1200px; height: 720px; overflow: hidden; }
  body {
    position: relative;
    font-family: "Arimo", Arial, sans-serif;
    background: var(--page-dark);
  }
  .field-backdrop {
    position: absolute; inset: 0;
    background: radial-gradient(ellipse at 50% 55%, #4f7a3a 0%, var(--field-green) 45%, var(--page-dark) 90%);
  }
  .site-panel {
    position: absolute; left: 140px; top: 20px; width: 919px; height: 646px;
    background: var(--panel-white); border-radius: 6px; overflow: hidden;
    box-shadow: 0 0 30px rgba(0,0,0,.6);
  }
  .site-header { position: relative; height: 102px; border-bottom: 2px solid var(--nav-line); }
  .brand {
    position: absolute; left: 14px; top: 38px;
    display: flex; align-items: center; gap: 10px;
    font-size: 26px; font-weight: 700; letter-spacing: 2px; color: var(--text-dark);
  }
  .brand-mark { width: 34px; height: 34px; border-radius: 50%; background: #9b1a2a; }
  .login-button {
    position: absolute; left: 624px; top: 24px; width: 75px; height: 30px;
    background: linear-gradient(#555, var(--button-dark)); color: var(--text-white);
    border: 1px solid #111; border-bottom: 3px solid var(--button-accent); border-radius: 4px;
    font-size: 17px; text-align: center; line-height: 25px;
  }
  .login-or { position: absolute; left: 707px; top: 32px; font-size: 12px; color: #777; }
  .social-button {
    position: absolute; left: 728px; top: 26px; width: 182px; height: 23px;
    background: var(--social-blue); color: var(--text-white); border: 1px solid #2f4680;
    font-size: 13px; font-weight: 700; text-align: center; line-height: 21px;
  }
  .join-prompt { position: absolute; left: 624px; top: 70px; font-size: 13px; color: var(--text-dark); }
  .join-prompt a { color: var(--link-blue); text-decoration: none; }
  .main-nav {
    height: 47px; background: var(--nav-dark); border-bottom: 1px solid var(--hero-line);
    display: flex; justify-content: flex-end; align-items: center; gap: 46px; padding-right: 36px;
  }
  .main-nav a { color: var(--text-white); font-size: 17px; font-weight: 700; text-decoration: none; }
  .main-nav a.is-current { border-bottom: 1px solid #888; padding-bottom: 2px; }
  .hero {
    position: absolute; left: 0; top: 149px; width: 100%; height: 431px;
    background: linear-gradient(var(--sky-top), var(--sky-bottom));
    text-align: center; color: var(--text-white);
  }
  .hero-title {
    margin-top: 14px; font-size: 45px; font-weight: 700; letter-spacing: -1px; line-height: 52px;
    text-shadow: 0 2px 3px rgba(0,0,0,.45);
  }
  .hero-tagline { font-size: 18px; font-weight: 700; line-height: 24px; text-shadow: 0 1px 2px rgba(0,0,0,.45); }
  .floor {
    position: absolute; left: 0; top: 580px; width: 100%; height: 66px;
    background: linear-gradient(var(--floor-top), var(--floor-bottom));
  }
  .hero-illustration {
    position: absolute; left: 266px; top: 262px; width: 386px; height: 380px;
    background:
      radial-gradient(ellipse 30% 48% at 28% 58%, var(--silver) 0%, rgba(220,220,220,.55) 55%, rgba(220,220,220,0) 100%),
      radial-gradient(ellipse 30% 40% at 78% 65%, var(--bronze) 0%, rgba(217,130,46,.55) 55%, rgba(217,130,46,0) 100%),
      radial-gradient(ellipse 36% 58% at 52% 45%, var(--gold-light) 0%, var(--gold-dark) 60%, rgba(167,128,31,0) 100%);
  }
  .site-footer {
    position: absolute; left: 150px; right: 155px; top: 683px;
    display: flex; justify-content: space-between; font-size: 12px; color: var(--text-white);
  }
  .footer-links a { color: var(--text-white); text-decoration: none; padding: 0 5px; }
</style>
</head>
<body>
  <div class="field-backdrop" role="img" aria-label="Blurred sports field with grass and white lines"></div>

  <div class="site-panel">
    <header class="site-header">
      <div class="brand"><span class="brand-mark"></span>MEDALNOOK</div>
      <div class="login-button">Login</div>
      <span class="login-or">or</span>
      <div class="social-button">Connect with chatterlane</div>
      <p class="join-prompt">Not a member yet? <a href="#">Click here to join</a></p>
    </header>

    <nav class="main-nav">
      <a href="#" class="is-current">Home</a>
      <a href="#">What?</a>
      <a href="#">Why?</a>
      <a href="#">Tour</a>
    </nav>

    <section class="hero">
      <h1 class="hero-title">Welcome to medalnook,</h1>
      <p class="hero-tagline">The newest online trophy store on the web.</p>
    </section>
    <div class="floor"></div>
    <div class="hero-illustration" role="img" aria-label="Silver, gold and bronze trophy cups standing side by side"></div>
  </div>

  <footer class="site-footer">
    <span>Copyright © 2011 medalnook, All rights reserved.</span>
    <span class="footer-links"><a href="#">About</a> | <a href="#">Privacy Policy</a> | <a href="#">Terms of Service</a> | <a href="#">Help</a></span>
  </footer>
</body>
</html>
```